Lume Hart Co Need a custom graphic

I need to have the attached chart re-designed in a hand colored pencil format. The heading needs to be changed to "The most effective methods for hiring sales people". Do not include the background logo in the sample file.

Place the attached Lume Hart Co logo next to the most effective methods (91%)

```html
<!DOCTYPE html>
<html lang="en">
<head>
<meta charset="utf-8">
<title>The Most Effective Methods for Hiring Sales People</title>
<link rel="stylesheet" href="https://fonts.googleapis.com/css2?family=Bebas+Neue&family=Oswald:wght@500&family=Architects+Daughter&display=swap">
<style>
  :root {
    --backdrop: #c8d1e0;
    --card: #ffffff;
    --band: #1b9ad6;
    --navy: #1c2a6b;
    --line-blue: #2a9ddb;
    --grid: #d9dde4;
    --white: #ffffff;
  }
  html, body {
    margin: 0;
    padding: 0;
    width: 1200px;
    height: 1200px;
    overflow: hidden;
    background: var(--backdrop);
  }
  .infographic {
    display: block;
    width: 1200px;
    height: 1200px;
  }
  .card { fill: var(--card); }
  .title-band { fill: var(--band); }
  .title-text {
    font-family: "Bebas Neue", "Oswald", sans-serif;
    font-size: 54px;
    fill: var(--white);
  }
  .grid-line { stroke: var(--grid); stroke-width: 1.5; }
  .axis-value {
    font-family: "Oswald", sans-serif;
    font-weight: 500;
    font-size: 20px;
    fill: var(--navy);
  }
  .axis-pill-dark { fill: var(--navy); }
  .axis-pill-light { fill: var(--band); }
  .axis-title {
    font-family: "Oswald", sans-serif;
    font-weight: 500;
    font-size: 20px;
    fill: var(--white);
  }
  .trend-line {
    fill: none;
    stroke: var(--line-blue);
    stroke-width: 3.5;
    stroke-linejoin: round;
    stroke-linecap: round;
  }
  .data-point {
    fill: var(--white);
    stroke: var(--navy);
    stroke-width: 2;
  }
  .percent {
    font-family: "Architects Daughter", cursive;
    font-size: 27px;
    font-weight: 700;
    fill: var(--line-blue);
    stroke: var(--line-blue);
    stroke-width: 0.6;
  }
  .method {
    font-family: "Architects Daughter", cursive;
    font-size: 15px;
    fill: var(--navy);
    stroke: var(--navy);
    stroke-width: 0.3;
    letter-spacing: 0.5px;
  }
  .brand-name {
    font-family: "Oswald", sans-serif;
    font-weight: 500;
    font-size: 30px;
    fill: var(--navy);
    letter-spacing: 1px;
  }
  .brand-mark { fill: var(--band); }
  .pointer-arrow {
    fill: none;
    stroke: var(--navy);
    stroke-width: 2.5;
    stroke-linecap: round;
  }
</style>
</head>
<body>
<svg class="infographic" viewBox="0 0 1200 1200" xmlns="http://www.w3.org/2000/svg">
  <rect class="card" x="46" y="215" width="1105" height="779"/>
  <rect class="title-band" x="46" y="215" width="1105" height="85"/>
  <text class="title-text" x="122" y="277" textLength="928" lengthAdjust="spacingAndGlyphs">THE MOST EFFECTIVE METHODS FOR HIRING SALES PEOPLE</text>

  <g class="chart-grid">
    <line class="grid-line" x1="184" y1="420" x2="1056" y2="420"/>
    <line class="grid-line" x1="184" y1="477" x2="1056" y2="477"/>
    <line class="grid-line" x1="184" y1="534" x2="1056" y2="534"/>
    <line class="grid-line" x1="184" y1="590" x2="1056" y2="590"/>
    <line class="grid-line" x1="184" y1="647" x2="1056" y2="647"/>
    <line class="grid-line" x1="184" y1="704" x2="1056" y2="704"/>
    <line class="grid-line" x1="184" y1="760" x2="1056" y2="760"/>
    <line class="grid-line" x1="184" y1="817" x2="1056" y2="817"/>
    <line class="grid-line" x1="184" y1="874" x2="1056" y2="874"/>
    <line class="grid-line" x1="184" y1="931" x2="1056" y2="931"/>
    <line class="grid-line" x1="184" y1="420" x2="184" y2="931"/>
    <line class="grid-line" x1="263" y1="420" x2="263" y2="931"/>
    <line class="grid-line" x1="343" y1="420" x2="343" y2="931"/>
    <line class="grid-line" x1="422" y1="420" x2="422" y2="931"/>
    <line class="grid-line" x1="502" y1="420" x2="502" y2="931"/>
    <line class="grid-line" x1="582" y1="420" x2="582" y2="931"/>
    <line class="grid-line" x1="661" y1="420" x2="661" y2="931"/>
    <line class="grid-line" x1="741" y1="420" x2="741" y2="931"/>
    <line class="grid-line" x1="820" y1="420" x2="820" y2="931"/>
    <line class="grid-line" x1="900" y1="420" x2="900" y2="931"/>
    <line class="grid-line" x1="980" y1="420" x2="980" y2="931"/>
    <line class="grid-line" x1="1056" y1="420" x2="1056" y2="931"/>
  </g>

  <g class="y-axis" text-anchor="end">
    <text class="axis-value" x="172" y="427">0.90</text>
    <text class="axis-value" x="172" y="484">0.80</text>
    <text class="axis-value" x="172" y="541">0.70</text>
    <text class="axis-value" x="172" y="597">0.60</text>
    <text class="axis-value" x="172" y="654">0.50</text>
    <text class="axis-value" x="172" y="711">0.40</text>
    <text class="axis-value" x="172" y="767">0.30</text>
    <text class="axis-value" x="172" y="824">0.20</text>
    <text class="axis-value" x="172" y="881">0.10</text>
    <text class="axis-value" x="172" y="938">0.00</text>
  </g>

  <rect class="axis-pill-dark" x="86" y="404" width="31" height="208" rx="15.5"/>
  <text class="axis-title" transform="translate(109 508) rotate(-90)" text-anchor="middle">PREDICTIVE VALIDITY</text>

  <rect class="axis-pill-light" x="890" y="943" width="169" height="34" rx="17"/>
  <text class="axis-title" x="974" y="967" text-anchor="middle">HIRING METHOD</text>

  <polyline class="trend-line" points="298,898 322,840 421,819 501,813 580,798 661,800 740,746 819,649 899,591 977,519 1056,435"/>

  <g class="data-points">
    <circle class="data-point" cx="298" cy="898" r="4.5"/>
    <circle class="data-point" cx="322" cy="840" r="4.5"/>
    <circle class="data-point" cx="421" cy="819" r="4.5"/>
    <circle class="data-point" cx="501" cy="813" r="4.5"/>
    <circle class="data-point" cx="580" cy="798" r="4.5"/>
    <circle class="data-point" cx="661" cy="800" r="4.5"/>
    <circle class="data-point" cx="740" cy="746" r="4.5"/>
    <circle class="data-point" cx="819" cy="649" r="4.5"/>
    <circle class="data-point" cx="899" cy="591" r="4.5"/>
    <circle class="data-point" cx="977" cy="519" r="4.5"/>
    <circle class="data-point" cx="1056" cy="435" r="4.5"/>
  </g>

  <g class="percent-labels" text-anchor="middle">
    <text class="percent" x="240" y="885">13%</text>
    <text class="percent" x="325" y="818">18%</text>
    <text class="percent" x="421" y="803">20%</text>
    <text class="percent" x="501" y="803">20%</text>
    <text class="percent" x="580" y="781">23%</text>
    <text class="percent" x="661" y="781">23%</text>
    <text class="percent" x="716" y="729">33%</text>
    <text class="percent" x="787" y="647">51%</text>
    <text class="percent" x="867" y="586">57%</text>
    <text class="percent" x="943" y="521">71%</text>
    <text class="percent" x="1040" y="420">91%</text>
  </g>

  <g class="method-labels">
    <text class="method" x="261" y="922" text-anchor="middle">CULTURE</text>
    <text class="method" x="261" y="940" text-anchor="middle">TEST</text>
    <text class="method" x="353" y="864">RESUME</text>
    <text class="method" x="421" y="724" text-anchor="middle">BEHAVIOR/</text>
    <text class="method" x="421" y="743" text-anchor="middle">PERSONALITY</text>
    <text class="method" x="421" y="762" text-anchor="middle">TEST</text>
    <text class="method" x="501" y="847" text-anchor="middle">TRADITIONAL</text>
    <text class="method" x="501" y="865" text-anchor="middle">INTERVIEW</text>
    <text class="method" x="575" y="724" text-anchor="middle">REFERENCE</text>
    <text class="method" x="575" y="743" text-anchor="middle">CHECK</text>
    <text class="method" x="698" y="827" text-anchor="middle">EMOTIONAL</text>
    <text class="method" x="698" y="845" text-anchor="middle">INTELLIGENCE</text>
    <text class="method" x="755" y="753">SKILLS TEST</text>
    <text class="method" x="833" y="659">GENERAL</text>
    <text class="method" x="833" y="677">MENTAL</text>
    <text class="method" x="833" y="695">ABILITY</text>
    <text class="method" x="916" y="602">HIGHLY STRUCTURED</text>
    <text class="method" x="916" y="620">INTERVIEW WITH</text>
    <text class="method" x="916" y="638">SCORE-CARD</text>
    <text class="method" x="994" y="533">MULTI</text>
    <text class="method" x="994" y="550">MEASUREMENT</text>
    <text class="method" x="994" y="567">ASSESSMENT</text>
  </g>

  <g class="brand-callout">
    <rect class="brand-mark" x="787" y="327" width="18" height="18"/>
    <text class="brand-name" x="813" y="346">LUME HART CO</text>
    <text class="method" x="789" y="386">SALES SPECIFIC MULTI</text>
    <text class="method" x="789" y="404">MEASUREMENT ASSESSMENT</text>
    <path class="pointer-arrow" d="M1024 332 Q1064 322 1078 356"/>
    <path class="pointer-arrow" d="M1022 323 L1024 332 L1032 338"/>
  </g>
</svg>
</body>
</html>
```